Commercial/Corporate Law Firm needs Website Design

Hi guys. I've started up a new law firm and would love your help designing an attractive website. I'll need both design and coding, and to make it easy for us to edit as necessary later, I think it should be built off a Wordpress.org structure.
FIRST IMPRESSIONS
It's very important that the first impression of the website really captures our prospective clients' attention and impresses them. Their first three seconds needs to be good.
I imagine the homepage may be short, with a menu bar and a compelling image, and with a tagline overlaid or underneath (eg. "It's about results.")
The image should be related to our practice areas: eg. IPOs, corporate transactions, or commercial negotiations.
I have previously suggested there could be a skyline image of Sydney or Adelaide. However, because we are based in Adelaide, I don't think Sydney is appropriate - and Adelaide is probably too boring to use.
HOMEPAGE
Being a new firm, we don't have many existing testimonials, and I will be the only lawyer to start with. So we need to focus on the nature of the services we will provide and how my experience can help them. We have an existing logo to use, and I would like the website colour scheme not to clash with that logo (dark blue and white).
After the initial image and tagline there should be a brief introduction to each of the main areas of work, eg. "We specialise in three main areas of practice:"
1. Corporate Transactions and Regulation
2. Business Law and Dispute Resolution
3. Migration Assistance
These should each have an appropriate photo and link to a separate page that briefly describes our services in that area.
Below that there should be a message from me with a photo. Finally, at the bottom, there should be a "Contact Us" section which shows a Google image of our address, contact details, and then our logo with colours inverted.
OTHER PAGES
While we will need some other pages, they should all be fairly simple. I think we will need one page to say "About Us", where I will put information about my experience. I think we will then need one page for each of the 3 areas listed above, which just needs an appropriate image and then text to describe the service. Finally, a "Contact Us" page which I imagine will be the same as the bottom of the homepage.
OTHER DETAILS
For now you can use details from my LinkedIn page to fill out any other text as necessary, or the photo.
Because the logo is square, I would prefer the design of the website also to be rectangular.
Looking forward to seeing your work! Thank you.
Good luck,
Marcus
Target Market(s)
Potential clients:
Businesses with legal issues or disputes
Companies wishing to list on the stock market

```html
<!DOCTYPE html>
<html lang="en">
<head>
<meta charset="utf-8">
<title>Marcus Varkalis – Varkalis Legal</title>
<link href="https://fonts.googleapis.com/css2?family=Montserrat:wght@600;700&family=Source+Sans+3:wght@400;600&family=Playfair+Display:ital@1&display=swap" rel="stylesheet">
<style>
  :root {
    --page-bg: #0e0e10;
    --footer-bg: #171726;
    --bottom-bg: #141422;
    --accent: #0a12e0;
    --link: #2c3f8f;
    --brand: #2f4f93;
    --text: #a9a9ad;
    --white: #ffffff;
    --rule: #2a2a3a;
    --icon: #7c7c84;
    --fb: #3b5aa8;
    --tw: #1da1e0;
    --gp: #d8432f;
  }
  * { box-sizing: border-box; margin: 0; padding: 0; }
  html, body { width: 886px; height: 1200px; overflow: hidden; }
  body { position: relative; background: var(--page-bg); font-family: "Source Sans 3", "Source Sans Pro", sans-serif; color: var(--text); }
  .abs { position: absolute; }

  .brand { display: flex; flex-direction: column; align-items: center; gap: 5px; color: var(--brand); font-family: "Source Sans 3", "Source Sans Pro", sans-serif; font-weight: 600; font-size: 12px; letter-spacing: 1.5px; line-height: 1; }
  .brand-square { width: 26px; height: 26px; background: var(--brand); }
  .brand-top { left: 36px; top: 11px; width: 90px; }

  .main-nav { right: 37px; top: 29px; display: flex; gap: 6px; align-items: center; }
  .main-nav a { font-family: "Montserrat", sans-serif; font-weight: 700; font-size: 9.5px; color: var(--white); text-decoration: none; padding: 3px 8px; line-height: 12px; }
  .main-nav a.active { border: 1.5px solid var(--white); padding: 3px 10px; }

  .portrait {
    left: 0; top: 215px; width: 560px; height: 774px;
    background:
      radial-gradient(ellipse 90px 120px at 175px 120px, rgba(120,88,70,.55), rgba(120,88,70,0) 100%),
      radial-gradient(ellipse 60px 200px at 210px 470px, rgba(200,200,210,.22), rgba(200,200,210,0) 100%),
      radial-gradient(ellipse 260px 470px at 210px 500px, #2f2d4c 0%, #24233c 55%, rgba(20,20,28,0) 100%);
  }

  .eyebrow { font-family: "Playfair Display", Georgia, serif; font-style: italic; color: var(--accent); font-size: 13px; }
  .role { left: 495px; top: 82px; }
  .name { left: 495px; top: 117px; font-family: "Montserrat", sans-serif; font-weight: 700; font-size: 36px; line-height: 47px; letter-spacing: 1px; color: var(--white); }
  .name .surname { color: var(--accent); display: block; }

  .bio { top: 251px; width: 156px; font-size: 13.6px; line-height: 17.3px; text-align: justify; }
  .bio p + p { margin-top: 15px; }
  .bio-left { left: 495px; }
  .bio-right { left: 679px; }
  .bio a { color: var(--link); text-decoration: none; }

  .contact-label { left: 495px; top: 747px; }
  .contact-list { left: 497px; top: 784px; list-style: none; font-size: 13.6px; line-height: 17.3px; }
  .contact-list li { display: flex; gap: 11px; margin-bottom: 12px; }
  .contact-list svg { flex: none; margin-top: 2px; }
  .contact-list .addr { width: 100px; }

  .signature { left: 681px; top: 760px; width: 146px; height: 78px;
    background: radial-gradient(ellipse 70px 30px at 50% 55%, rgba(190,190,200,.18), rgba(190,190,200,0) 100%); }

  .social { left: 495px; top: 938px; display: flex; gap: 14px; }
  .social span { width: 10px; height: 10px; border-radius: 50%; background: #4d4d54; }

  .site-footer { left: 0; top: 989px; width: 886px; height: 166px; background: var(--footer-bg); }
  .brand-foot { left: 393px; top: 1026px; width: 100px; font-size: 13px; }
  .brand-foot .brand-square { width: 34px; height: 34px; }
  .footer-social { left: 0; width: 886px; top: 1094px; display: flex; justify-content: center; gap: 14px; }
  .footer-social span { width: 17px; height: 17px; border-radius: 50%; }

  .bottom-bar { left: 0; top: 1154px; width: 886px; height: 46px; background: var(--bottom-bg); border-top: 1px solid var(--rule); font-size: 12.2px; color: #c9c9cf; }
  .copyright { left: 156px; top: 14px; }
  .copyright strong { color: var(--white); font-weight: 600; }
  .legal-links { left: 517px; top: 14px; display: flex; gap: 10px; }
  .legal-links a { color: #c9c9cf; text-decoration: none; }
</style>
</head>
<body>
  <header>
    <div class="brand brand-top abs"><span class="brand-square"></span>VARKALIS LEGAL</div>
    <nav class="main-nav abs">
      <a class="active" href="#">OUR ATTORNEY</a>
      <a href="#">OUR SERVICES</a>
      <a href="#">FAQS</a>
      <a href="#">CONTACT US</a>
    </nav>
  </header>

  <div class="portrait abs" role="img" aria-label="Portrait of Marcus Varkalis smiling, in a dark navy suit, white shirt and red tie"></div>

  <main>
    <div class="eyebrow role abs">- Principal -</div>
    <h1 class="name abs">MARCUS <span class="surname">VARKALIS</span></h1>

    <div class="bio bio-left abs">
      <p>Marcus was admitted to practice in the Supreme Court of South Australia in April 2009. He also met the requirements for admission to the State Bar of California in February 2014.</p>
      <p>Marcus holds a Bachelor of Laws (with First Class Honours), a Bachelor of Commerce from the <a href="#">Southgate University</a>, and a Master of Applied Finance from Meridian Professional. He also studied at Eastlake University in Beijing, where he worked as a consultant for a Chinese carbon credits broker.</p>
    </div>
    <div class="bio bio-right abs">
      <p>Marcus commenced practicing law for the <a href="#">National Markets Commission (NMC)</a> in February 2010. In this role Marcus was responsible for reviewing public debt and equity fundraisings, takeover bids, and schemes of arrangement by large SMX 200 companies, as well as those of smaller listed and unlisted companies.</p>
      <p>Marcus has been responsible for teaching commercial law at a postgraduate level as Lecturer-in-Charge at the Southgate University. He is a director of Lexicon Learning, which specialises in developing mobile applications for education in law.</p>
    </div>

    <div class="eyebrow contact-label abs">- Contact us -</div>
    <ul class="contact-list abs">
      <li>
        <svg width="12" height="14" viewBox="0 0 12 14" fill="none" stroke="var(--icon)" stroke-width="1.2"><path d="M6 13s4.5-4.6 4.5-7.5a4.5 4.5 0 0 0-9 0C1.5 8.4 6 13 6 13z"/><circle cx="6" cy="5.5" r="1.6"/></svg>
        <span class="addr">Varkalis Legal/Adelaide/ Australia.</span>
      </li>
      <li>
        <svg width="12" height="14" viewBox="0 0 12 14" fill="none" stroke="var(--icon)" stroke-width="1.2"><path d="M1.5 10V7a4.5 4.5 0 0 1 9 0v3"/><rect x="1" y="8.5" width="2.5" height="3.5" rx="1"/><rect x="8.5" y="8.5" width="2.5" height="3.5" rx="1"/></svg>
        <span>+1 555-014-2235</span>
      </li>
      <li>
        <svg width="12" height="14" viewBox="0 0 12 14" fill="none" stroke="var(--icon)" stroke-width="1.2"><rect x="0.8" y="3.5" width="10.4" height="7.5"/><path d="M0.8 3.5 6 8l5.2-4.5"/></svg>
        <span>marcus@varkalislegal.com</span>
      </li>
    </ul>

    <div class="signature abs" role="img" aria-label="Handwritten signature of Marcus Varkalis"></div>

    <div class="social abs"><span></span><span></span><span></span><span></span></div>
  </main>

  <footer>
    <div class="site-footer abs"></div>
    <div class="brand brand-foot abs"><span class="brand-square"></span>VARKALIS LEGAL</div>
    <div class="footer-social abs">
      <span style="background:var(--fb)"></span>
      <span style="background:var(--tw)"></span>
      <span style="background:var(--gp)"></span>
    </div>
    <div class="bottom-bar abs">
      <div class="copyright abs">© Copyright 2018 <strong>Varkalis Legal</strong></div>
      <nav class="legal-links abs">
        <a href="#">Support</a><span>|</span>
        <a href="#">Contact Us</a><span>|</span>
        <a href="#">Disclaimer</a><span>|</span>
        <a href="#">Privacy Policy</a>
      </nav>
    </div>
  </footer>
</body>
</html>
```